Experienced Home remodel service

I'm a home remodeler. I want a catch phrase that clearly describes viewers what kind of work I'm in like the purple phrase on my rough draft idea. I need my website, phone, logo, slogan included. The picture is of my daughter. I want her on it. Be cool if something could be added to her picture like a hard hat or tool belt ect and her picture cut out/background removed. Some kind of background other than plain white for whole picture. I added extra pics of her so pick one

Target Market(s)

Home owners between 30-60

Industry/Entity Type

Home renovation/remodel

Colors

Designer to choose colors to be used in the design.

Requirements
Must have
• Daughters picture incorporated. Logo, phone, website address, slogan,
Nice to have
• See a hardhat or tool belt added to one of my daughters pictures that is chosen to use by designer

```html
<!DOCTYPE html>
<html lang="en">
<head>
<meta charset="utf-8">
<title>Brightline Remodeling – Billboard</title>
<link href="https://fonts.googleapis.com/css2?family=Kaushan+Script&family=Poppins:wght@500;600;700&display=swap" rel="stylesheet">
<style>
  :root {
    --page: #333333;
    --ink: #000000;
    --paper: #ffffff;
    --violet: #8a55ee;
    --lilac-light: #e9dcf7;
    --lilac-mid: #cdb8ee;
  }
  html, body {
    margin: 0;
    width: 1130px;
    height: 1200px;
    overflow: hidden;
    background: var(--page);
  }
  .billboard {
    position: absolute;
    left: 35px;
    top: 348px;
    width: 1060px;
    height: 504px;
    background: var(--ink);
    overflow: hidden;
  }
  .accent-column {
    position: absolute;
    left: 65px;
    top: 0;
    width: 299px;
    height: 100%;
    background: var(--violet);
  }
  .contact-band {
    position: absolute;
    left: 422px;
    top: 362px;
    right: 0;
    bottom: 0;
    background: var(--paper);
  }
  .portrait {
    position: absolute;
    left: 0;
    top: 12px;
    width: 448px;
    height: 492px;
    border-radius: 150px 150px 0 40px;
    background: linear-gradient(180deg, #e7c73a 0%, #c9a27a 28%, var(--lilac-mid) 55%, var(--lilac-light) 100%);
  }
  .brand {
    position: absolute;
    left: 510px;
    top: 36px;
    width: 530px;
    display: flex;
    align-items: center;
    justify-content: center;
    gap: 16px;
    color: var(--paper);
    font-family: 'Poppins', sans-serif;
    line-height: 1;
  }
  .brand-mark {
    width: 38px;
    height: 38px;
    background: var(--violet);
    flex: none;
  }
  .brand-text { display: flex; flex-direction: column; align-items: center; }
  .brand-name {
    font-weight: 600;
    font-size: 30px;
    letter-spacing: 0.5px;
  }
  .brand-slogan {
    font-weight: 500;
    font-size: 16px;
    letter-spacing: 3px;
    margin-top: 8px;
  }
  .headline {
    position: absolute;
    left: 410px;
    top: 130px;
    width: 630px;
    margin: 0;
    text-align: center;
    font-family: 'Kaushan Script', cursive;
    font-weight: 400;
    font-size: 74px;
    line-height: 88px;
    color: var(--paper);
    text-shadow: 3px 3px 0 var(--violet);
  }
  .headline span { display: block; }
  .headline .line-two { padding-right: 20px; }
  .web-ribbon {
    position: absolute;
    left: 479px;
    top: 338px;
    width: 532px;
    height: 60px;
    background: var(--violet);
    clip-path: polygon(3% 0, 100% 0, 97% 100%, 0 100%);
    display: flex;
    align-items: center;
    justify-content: center;
    font-family: 'Poppins', sans-serif;
    font-weight: 500;
    font-size: 28px;
    color: var(--paper);
  }
  .phone {
    position: absolute;
    left: 474px;
    top: 418px;
    display: flex;
    align-items: center;
    gap: 20px;
    font-family: 'Poppins', sans-serif;
    font-weight: 700;
    font-size: 54px;
    letter-spacing: 1px;
    color: var(--ink);
    line-height: 1;
  }
  .phone svg { width: 42px; height: 42px; }
</style>
</head>
<body>
  <main class="billboard">
    <div class="accent-column"></div>
    <div class="contact-band"></div>
    <div class="portrait" role="img" aria-label="Cut-out photo of a smiling girl in a yellow hard hat and lilac puffer jacket holding a hammer"></div>

    <div class="brand">
      <span class="brand-mark" aria-hidden="true"></span>
      <div class="brand-text">
        <span class="brand-name">BRIGHTLINE REMODELING</span>
        <span class="brand-slogan">PLAN-BUILD-FINISH</span>
      </div>
    </div>

    <h1 class="headline">
      <span class="line-one">For All Your Home</span>
      <span class="line-two">Remodel Needs</span>
    </h1>

    <div class="web-ribbon">BrightlineRemodeling.com</div>

    <div class="phone">
      <svg viewBox="0 0 24 24" aria-hidden="true">
        <path d="M6.6 2.5l2.6 3.8c.4.6.3 1.3-.2 1.8l-1.6 1.5c1 2.3 2.8 4.1 5.1 5.1l1.5-1.6c.5-.5 1.2-.6 1.8-.2l3.8 2.6c.6.4.8 1.2.4 1.8l-1.2 2c-.6 1-1.8 1.5-2.9 1.2C9.7 19.1 4.9 14.3 3.5 8.1c-.3-1.1.2-2.3 1.2-2.9l2-1.2z" fill="#000"/>
        <path d="M14 3.5a6.5 6.5 0 0 1 6.5 6.5M14 6.8a3.2 3.2 0 0 1 3.2 3.2" stroke="#000" stroke-width="2" fill="none" stroke-linecap="round"/>
      </svg>
      <span>555-0142-7386</span>
    </div>
  </main>
</body>
</html>
```